Professional Gearline Web Design

Project Brief: Website Redesign for Mechanical Design Consultancy
Project Overview
I want to update and improve my current website to create a more professional, modern, and high-credibility online presence for my mechanical design consultancy.

Current site: https://valtrobuild.design/

The new website must communicate expertise, precision, and trust—matching the standard of top engineering and product design agencies.

Reference Websites (Style + Structure Inspiration)
These represent the quality, cleanliness, and professionalism I want to achieve:

https://plinthformworks.com/
https://www.zorvanta.com/
https://quellory-uk.com/
Brand Look
Professional, modern, engineering-focused aesthetic
Clean layouts and strong typography
High-quality imagery conveying precision, innovation, and mechanical expertise
Colour scheme and styling must follow my existing logo (attached in project)
Platform Requirements
The website must be built on WordPress
Should use a clean, flexible theme or modern page builder (Elementor, Gutenberg, Bricks, or similar)
Avoid overly complex custom coding so I can easily edit content later
Final deliverable must allow me to manage and update content without developer assistance
Functionality
Fast-loading, lightweight, and smooth user experience
Clean animations and transitions similar to the reference sites
Fully mobile responsive
Clear navigation and strong visual hierarchy
Contact forms optimised for lead generation
Optional: subtle scroll effects, case study sliders, icon animations, etc.
SEO Aspirations
Developer should recommend and implement a modern SEO strategy
Proper on-page SEO setup (titles, meta, schema, alt tags, heading structure)
Optimised site architecture for ranking and crawling
Aim: Generate leads through improved visibility and keyword targeting
Optional but useful: Google Analytics, Google Search Console setup
User Journeys
(Recommended structure)

The site should be crafted around clear, intuitive journeys for each type of visitor:

Potential new clients
Quickly understand what services I offer
View examples of past work / case studies
See credibility indicators (process, expertise, industries served)
Easily contact me or request a project discussion
Returning clients
Access updated portfolio items
Find contact details or book follow-up work easily
General visitors discovering through SEO
Be guided to valtro service areas
Understand my value proposition quickly
Be invited to learn more or make contact
The developer should design the structure to support these journeys smoothly.

Maintenance Expectations
Website will be maintained by me, so it should be easy to update using relatively basic WordPress skills
Use modular templates and simple backend structure
Avoid unnecessary plugins
Provide brief handover documentation if required
Hosting Preferences
Site is currently hosted via a family member
Open to discussing moving to a paid, reliable hosting provider if preferable for performance and maintainability
Developer may advise on the best hosting setup for WordPress
Content
Most content can be taken from the existing website
Developer is welcome to suggest improvements to structure, layout, and imagery
Must remain easy for me to edit or add new content later (e.g., new projects)
Deliverables
Fully built WordPress website
Clean, professional, modern design inspired by the reference sites
Mobile-responsive across all devices
SEO-ready structure and optimisations
Transfer of website and admin rights
Any design assets, templates, or documentation used

```html
<!DOCTYPE html>
<html lang="en">
<head>
<meta charset="utf-8">
<title>Valtro Mechanical Design</title>
<link href="https://fonts.googleapis.com/css2?family=Bebas+Neue&family=Lexend:wght@300;400;500;600&display=swap" rel="stylesheet">
<style>
:root{
  --blue:#3058e8;
  --blue-dark:#2447c9;
  --ink:#1b1b1b;
  --text:#3a3a3a;
  --muted:#5c5c5c;
  --grey-bg:#f2f2f2;
  --line:#d9dff2;
  --white:#ffffff;
}
*{margin:0;padding:0;box-sizing:border-box}
html,body{width:1200px;height:4515px;overflow:hidden}
body{font-family:"Lexend",sans-serif;color:var(--text);background:var(--white)}
.page{position:relative;width:1200px;height:4515px;overflow:hidden}
section,header,footer,nav{position:absolute;left:0;width:1200px}
.btn{position:absolute;display:flex;align-items:center;justify-content:center;color:var(--white);font-size:14px;font-weight:400}
.btn-blue{background:var(--blue)}
.btn-dark{background:#444}
.section-title{position:absolute;left:0;width:1200px;text-align:center;font-size:40px;font-weight:500;color:#3b3b3b}
.section-title em{font-style:normal;color:var(--blue)}
.title-rule{position:absolute;height:3px;background:var(--blue);width:70px}

/* header */
.topbar{top:0;height:100px;background:var(--ink)}
.topbar-blue{position:absolute;left:560px;top:0;width:640px;height:100px;background:var(--blue);clip-path:polygon(40px 0,100% 0,100% 100%,0 100%)}
.brand{position:absolute;left:138px;top:8px;display:flex;align-items:center;gap:14px}
.brand-dot{width:86px;height:86px;border-radius:50%;background:var(--blue)}
.brand-name{color:var(--white);font-size:44px;font-weight:400;letter-spacing:6px;line-height:1}
.brand-sub{color:var(--white);font-size:11px;letter-spacing:2.4px;margin-top:6px}
.top-info{position:absolute;top:30px;display:flex;align-items:center;gap:12px;color:var(--white);font-size:14px;line-height:1.35}
.top-info small{font-size:11px;display:block}
.info-icon{width:40px;height:40px;border-radius:50%;background:var(--white);display:flex;align-items:center;justify-content:center}

.mainnav{top:100px;height:49px;background:var(--white);border-bottom:1px solid #e4e4e4}
.mainnav a{position:absolute;top:16px;font-size:13px;color:var(--ink);text-decoration:none}
.mainnav a.active{color:var(--blue)}
.mainnav a.active::after{content:"";position:absolute;left:0;right:0;bottom:-4px;height:1px;background:var(--blue)}

/* hero */
.hero{top:149px;height:529px;background:radial-gradient(ellipse at 50% 40%,#3a3a3a 0%,#171717 70%,#0c0c0c 100%)}
.hero-photo{position:absolute;left:306px;top:254px;width:588px;height:275px;background:linear-gradient(180deg,#5a5650 0%,#8a8377 35%,#4b463f 70%,#2a2724 100%);border-radius:40px 40px 0 0}
.hero h1{position:absolute;left:0;width:1200px;top:42px;text-align:center;font-family:"Bebas Neue",sans-serif;font-weight:400;color:var(--white);font-size:94px;line-height:88px;letter-spacing:1px}
.hero-sub{position:absolute;left:0;width:1200px;top:217px;text-align:center;color:var(--white);font-size:25px;font-weight:300}
.hero .btn{left:512px;top:273px;width:159px;height:48px;font-size:21px}

/* why */
.why{top:678px;height:426px}
.why-badge{position:absolute;left:1014px;top:26px;width:146px;height:146px;border-radius:50%;border:4px solid var(--blue);background:var(--white);padding:6px}
.why-badge div{width:100%;height:100%;border-radius:50%;background:radial-gradient(circle,#d9d9d9,#f4f4f4)}
.card{position:absolute;top:172px;width:222px;height:219px;border:1px solid #dfe4f4;background:var(--white);text-align:center;padding-top:28px}
.card svg{display:block;margin:0 auto}
.card h3{margin-top:18px;font-size:15px;font-weight:400;color:var(--blue);line-height:22px}
.card hr{width:40px;border:0;border-top:1px solid var(--blue);margin:8px auto 10px}
.card p{font-size:12.5px;line-height:21px;color:var(--text)}
.card.active{background:var(--blue)}
.card.active h3,.card.active p{color:var(--white)}
.card.active hr{border-color:var(--white)}

/* about */
.about{top:1104px;height:526px}
.about-photo{position:absolute;left:156px;top:74px;width:360px;height:360px;border-radius:50%;background:radial-gradient(circle at 50% 40%,#9aa3b0 0%,#6c7584 45%,#3b4352 100%)}
.about-photo span{position:absolute;left:120px;top:300px;color:var(--white);font-size:20px;font-style:italic;transform:rotate(-12deg)}
.about-kicker{position:absolute;left:560px;top:50px;font-size:24px;color:var(--blue);font-weight:500}
.about-title{position:absolute;left:553px;top:80px;font-size:41px;font-weight:400;color:#333}
.about-title em{font-style:normal;color:var(--blue)}
.about-copy{position:absolute;left:561px;width:486px;font-size:13.5px;line-height:25.5px;color:var(--ink)}
.about-copy b{font-weight:400;color:var(--blue)}
.vision{position:absolute;left:560px;top:288px;font-size:24px;font-weight:500;color:#333}
.vision em{font-style:normal;color:var(--blue)}

/* services */
.services{top:1630px;height:740px;background:var(--grey-bg)}
.orbit{position:absolute;left:0;top:0}
.svc-node{position:absolute;width:74px;height:74px;border-radius:50%;background:var(--white);border:1px solid #c9c9c9;display:flex;align-items:center;justify-content:center}
.svc-label{position:absolute;font-size:16px;color:var(--blue);line-height:25px}
.hub{position:absolute;left:468px;top:245px;width:238px;height:238px;border-radius:50%;background:var(--white);box-shadow:0 4px 18px rgba(0,0,0,.18);display:flex;align-items:center;justify-content:center}
.hub-core{width:198px;height:198px;border-radius:50%;background:var(--blue);display:flex;align-items:center;justify-content:center;color:var(--white);font-size:34px;letter-spacing:3px}

/* feedback */
.feedback{top:2370px;height:468px}
.quote-card{position:absolute;left:193px;top:149px;width:825px;height:211px;background:var(--white);box-shadow:0 2px 14px rgba(0,0,0,.12);text-align:center}
.quote-card p{position:absolute;left:0;right:0;top:38px;font-size:13px;line-height:28px;color:var(--ink);padding:0 30px}
.quote-card h4{position:absolute;left:0;right:0;top:162px;font-size:15px;font-weight:500;color:var(--blue)}
.arrows{position:absolute;left:576px;top:378px}

/* portfolio */
.portfolio{top:2838px;height:610px;background:var(--blue)}
.portfolio .section-title{color:var(--white)}
.work{position:absolute;top:165px;width:294px;height:291px;background:var(--white)}
.work-img{position:absolute;left:34px;top:22px;width:226px;height:200px}
.work h3{position:absolute;left:0;right:0;top:251px;text-align:center;font-size:16px;font-weight:500;color:var(--blue)}
.round-arrow{position:absolute;width:36px;height:36px;border-radius:50%;background:var(--white);display:flex;align-items:center;justify-content:center;box-shadow:0 1px 5px rgba(0,0,0,.2)}

/* clients */
.clients{top:3448px;height:432px}
.clients-sub{position:absolute;left:0;width:1200px;top:142px;text-align:center;font-size:14px;color:var(--ink)}
.client{position:absolute;top:196px;width:172px;height:112px;background:var(--white);box-shadow:0 2px 10px rgba(0,0,0,.12);display:flex;align-items:center;justify-content:center;gap:8px;font-size:19px;color:#333}
.client i{width:14px;height:14px;background:var(--blue);display:block}

/* cta */
.cta{top:3880px;height:430px}
.cta h2{position:absolute;left:140px;top:160px;font-size:42px;font-weight:500;color:var(--blue)}
.cta p{position:absolute;left:144px;top:218px;font-size:15.5px;line-height:33px;color:var(--ink)}
.cta .btn{left:144px;top:281px;width:126px;height:39px;font-size:15px}
.cta-halo{position:absolute;left:720px;top:70px;width:260px;height:260px;border-radius:50%;background:#e9edf8}
.cta-photo{position:absolute;left:604px;top:44px;width:465px;height:386px;background:linear-gradient(180deg,#c49b7d 0%,#7f6a58 45%,#4d5d80 100%);border-radius:200px 200px 0 0}

/* footer */
.footer{top:4310px;height:205px;background:var(--blue)}
.footer-dark{position:absolute;left:0;top:0;width:330px;height:205px;background:var(--ink);border-radius:0 205px 0 0}
.footer-photo{position:absolute;left:140px;top:-2px;width:204px;height:204px;border-radius:50%;border:10px solid var(--ink);background:radial-gradient(circle,#6e88a8,#304460)}
.footer-nav a{position:absolute;top:29px;color:var(--white);font-size:13px;text-decoration:none}
.f-item{position:absolute;top:86px;display:flex;align-items:center;gap:14px;color:var(--white);font-size:11px;line-height:17px}
.f-ico{width:30px;height:30px;border-radius:50%;background:var(--white);display:flex;align-items:center;justify-content:center}
.socials{position:absolute;left:870px;top:150px;display:flex;gap:7px}
.socials span{width:27px;height:27px;border:1.5px solid var(--white)}
.copy{position:absolute;left:377px;top:157px;color:var(--white);font-size:12px}
</style>
</head>
<body>
<div class="page">

<header class="topbar">
  <div class="topbar-blue"></div>
  <div class="brand">
    <div class="brand-dot"></div>
    <div><div class="brand-name">valtro</div><div class="brand-sub">MECHANICAL DESIGN</div></div>
  </div>
  <div class="top-info" style="left:608px">
    <div class="info-icon"><svg width="22" height="22" viewBox="0 0 24 24" fill="none" stroke="#3058e8" stroke-width="2"><circle cx="12" cy="12" r="9"/><circle cx="12" cy="12" r="4"/></svg></div>
    <div>11+ Years<br>Multi-Industry Expertise</div>
  </div>
  <div class="top-info" style="left:851px">
    <div class="info-icon"><svg width="20" height="20" viewBox="0 0 24 24" fill="none" stroke="#3058e8" stroke-width="2"><path d="M5 3h4l2 5-3 2a12 12 0 0 0 6 6l2-3 5 2v4a2 2 0 0 1-2 2A18 18 0 0 1 3 5a2 2 0 0 1 2-2z"/></svg></div>
    <div><small>Call Us</small>+44 (0) 7700 900321</div>
  </div>
</header>

<nav class="mainnav">
  <a class="active" style="left:276px">Home</a>
  <a style="left:363px">Why Choose Us</a>
  <a style="left:511px">About Us</a>
  <a style="left:619px">Services</a>
  <a style="left:719px">Our Portfolio</a>
  <a style="left:850px">Contact Us</a>
</nav>

<section class="hero">
  <div class="hero-photo" role="img" aria-label="Cutaway of a dual clutch transmission assembly"></div>
  <h1>DUAL CLUTCH<br>TRANSMISSION DESIGN</h1>
  <div class="hero-sub">Highly complex mechanical systems</div>
  <a class="btn btn-blue">Contact Us</a>
</section>

<section class="why">
  <h2 class="section-title" style="top:74px">Why <em>Choose Us</em></h2>
  <div class="title-rule" style="left:553px;top:132px"></div>
  <div class="why-badge"><div role="img" aria-label="Go-kart simulator rig render"></div></div>

  <div class="card" style="left:142px">
    <svg width="44" height="44" viewBox="0 0 44 44" fill="none" stroke="#3058e8" stroke-width="1.6"><circle cx="22" cy="20" r="8"/><path d="M18 30h8M19 34h6M22 4v5M8 20H4M40 20h-4M11 9l3 3M33 9l-3 3"/></svg>
    <h3>End-to-End Product<br>Development</h3><hr><p>From Concept To<br>Production-ready Design.</p>
  </div>
  <div class="card active" style="left:373px">
    <svg width="44" height="44" viewBox="0 0 44 44" fill="none" stroke="#fff" stroke-width="1.6"><circle cx="22" cy="22" r="14"/><circle cx="22" cy="22" r="6"/><path d="M22 4v4M22 36v4M4 22h4M36 22h4"/></svg>
    <h3>11+ Years<br>Multi-Industry Expertise</h3><hr><p>Automotive, Consumer,<br>Medical, Industrial &amp; More.</p>
  </div>
  <div class="card" style="left:604px">
    <svg width="44" height="44" viewBox="0 0 44 44" fill="none" stroke="#3058e8" stroke-width="1.6"><rect x="6" y="8" width="32" height="22"/><path d="M16 38h12M22 30v8M12 14h10v10H12zM26 14h6M26 20h6"/></svg>
    <h3>High-Quality CAD,<br>Drawings &amp; Renders</h3><hr><p>Precise Engineering Output<br>Every Time.</p>
  </div>
  <div class="card" style="left:837px">
    <svg width="44" height="44" viewBox="0 0 44 44" fill="none" stroke="#3058e8" stroke-width="1.6"><circle cx="22" cy="14" r="7"/><circle cx="22" cy="14" r="3"/><path d="M6 30c6-4 10-4 16 0l8-2c3 0 3 3 0 4l-10 4-14-2"/></svg>
    <h3>Professional<br>Project Management</h3><hr><p>Smooth Coordination From<br>Design To Production.</p>
  </div>
</section>

<section class="about">
  <div class="about-photo" role="img" aria-label="Portrait of chief engineer Rowan Hale"><span>Rowan Hale</span></div>
  <div class="about-kicker">About</div>
  <h2 class="about-title">Valtro <em>Mechanical Design</em></h2>
  <p class="about-copy" style="top:142px"><b>Rowan Hale</b> is the Chief Engineer at Valtro Mechanical Design. He has 11 years experience working as a mechanical design engineer in multiple industries including high performance automotive, consumer products, medical, industrial plus many more. He has worked in multiple roles across a wide range of products.</p>
  <h3 class="vision">My <em>Vision</em></h3>
  <p class="about-copy" style="top:334px">To be the go-to partner for turning bold ideas into precision engineered products &amp; delivering end-to-end mechanical design excellence, manufacturability, and reliability across industries.</p>
  <a class="btn btn-dark" style="left:562px;top:411px;width:127px;height:39px">Contact Us</a>
</section>

<section class="services">
  <h2 class="section-title" style="top:74px">Services <em>We Provide</em></h2>
  <div class="title-rule" style="left:568px;top:132px"></div>
  <svg class="orbit" width="1200" height="740"><circle cx="587" cy="364" r="178" fill="none" stroke="#666" stroke-width="1.2" stroke-dasharray="3 4"/></svg>
  <div class="hub"><div class="hub-core">valtro</div></div>

  <div class="svc-node" style="left:459px;top:173px"><svg width="34" height="34" viewBox="0 0 34 34" fill="none" stroke="#3058e8" stroke-width="1.5"><rect x="8" y="8" width="12" height="8"/><path d="M14 16v12M20 12h8M26 9l4 3-4 3"/></svg></div>
  <div class="svc-node" style="left:629px;top:169px"><svg width="34" height="34" viewBox="0 0 34 34" fill="none" stroke="#3058e8" stroke-width="1.5"><circle cx="12" cy="12" r="6"/><circle cx="12" cy="12" r="2"/><path d="M20 28V18M24 28V14M28 28V20M4 28h26"/></svg></div>
  <div class="svc-node" style="left:720px;top:292px"><svg width="34" height="34" viewBox="0 0 34 34" fill="none" stroke="#3058e8" stroke-width="1.5"><circle cx="17" cy="12" r="6"/><circle cx="17" cy="12" r="2"/><path d="M4 20l8 8h10l8-8"/></svg></div>
  <div class="svc-node" style="left:687px;top:441px"><svg width="34" height="34" viewBox="0 0 34 34" fill="none" stroke="#3058e8" stroke-width="1.5"><path d="M17 5l11 6v12l-11 6-11-6V11z M17 17l11-6M17 17v12M17 17L6 11"/></svg></div>
  <div class="svc-node" style="left:543px;top:500px"><svg width="34" height="34" viewBox="0 0 34 34" fill="none" stroke="#3058e8" stroke-width="1.5"><rect x="6" y="4" width="20" height="26"/><path d="M10 10h4M10 16h4M10 22h4M17 10h6M17 16h6M17 22h6"/></svg></div>
  <div class="svc-node" style="left:401px;top:427px"><svg width="34" height="34" viewBox="0 0 34 34" fill="none" stroke="#3058e8" stroke-width="1.5"><circle cx="17" cy="12" r="6"/><circle cx="17" cy="12" r="2"/><path d="M4 26h26M6 26v-4h4v4M14 26v-4h4v4M22 26v-4h4v4"/></svg></div>
  <div class="svc-node" style="left:371px;top:286px"><svg width="34" height="34" viewBox="0 0 34 34" fill="none" stroke="#3058e8" stroke-width="1.5"><path d="M20 6l4 4-10 10-4-4z M12 18l-4 10M24 6l4-2"/></svg></div>

  <div class="svc-label" style="left:357px;top:196px">Painting</div>
  <div class="svc-label" style="left:723px;top:196px">Mechanical Design</div>
  <div class="svc-label" style="left:814px;top:319px">Design Consultancy</div>
  <div class="svc-label" style="left:783px;top:476px">3D Printing</div>
  <div class="svc-label" style="left:512px;top:583px">Project Management</div>
  <div class="svc-label" style="left:224px;top:450px;text-align:right;width:160px">Design for<br>Manufacture (DFM)</div>
  <div class="svc-label" style="left:255px;top:315px">TIG Welding</div>

  <a class="btn btn-blue" style="left:529px;top:642px;width:126px;height:41px">Contact Us</a>
</section>

<section class="feedback">
  <h2 class="section-title" style="top:58px">Real Feedback <em>From Real Clients</em></h2>
  <div class="title-rule" style="left:586px;top:116px"></div>
  <div class="quote-card">
    <p>Rowan is able to bridge the gap between what management want and what manufacturing can deliver. In the field of Casting his intuition for the process and knowledge of costing technical nuances means he is able to push both the design and guide manufacturers to produce excellent results.”</p>
    <h4>Dean Marlow, Design Engineer</h4>
  </div>
  <svg class="arrows" width="56" height="22" viewBox="0 0 56 22" fill="none" stroke-width="2"><path d="M24 11H4M10 5l-6 6 6 6" stroke="#222"/><path d="M30 11h20M44 5l6 6-6 6" stroke="#3058e8"/></svg>
</section>

<section class="portfolio">
  <h2 class="section-title" style="top:78px">Our Work Portfolio</h2>
  <div class="round-arrow" style="left:96px;top:289px"><svg width="12" height="12" viewBox="0 0 12 12" fill="none" stroke="#222" stroke-width="2"><path d="M8 2L4 6l4 4"/></svg></div>
  <div class="round-arrow" style="left:1070px;top:292px"><svg width="12" height="12" viewBox="0 0 12 12" fill="none" stroke="#222" stroke-width="2"><path d="M4 2l4 4-4 4"/></svg></div>
  <div class="work" style="left:142px"><div class="work-img" role="img" aria-label="Industrial machine cabinet" style="background:linear-gradient(180deg,#c7ccd2,#7d8690)"></div><h3>3-Piece Alloy Wheels</h3></div>
  <div class="work" style="left:452px"><div class="work-img" role="img" aria-label="Go-kart simulator frame" style="background:linear-gradient(180deg,#eef0e4,#3a3a3a)"></div><h3>Go-Kart Simulator Design</h3></div>
  <div class="work" style="left:762px"><div class="work-img" role="img" aria-label="Polished alloy wheel" style="background:radial-gradient(circle,#3a3a3a 20%,#c8c8c8 45%,#8b8b8b 70%,#fff 72%)"></div><h3>Electrical Switchgear</h3></div>
  <a class="btn btn-dark" style="left:540px;top:491px;width:126px;height:38px">Contact Us</a>
</section>

<section class="clients">
  <h2 class="section-title" style="top:76px">Our <em>Happy Clients</em></h2>
  <div class="title-rule" style="left:500px;top:134px"></div>
  <div class="clients-sub">Chosen by businesses seeking high-quality engineering solutions.</div>
  <div class="round-arrow" style="left:87px;top:236px"><svg width="12" height="12" viewBox="0 0 12 12" fill="none" stroke="#222" stroke-width="2"><path d="M8 2L4 6l4 4"/></svg></div>
  <div class="round-arrow" style="left:1061px;top:240px"><svg width="12" height="12" viewBox="0 0 12 12" fill="none" stroke="#222" stroke-width="2"><path d="M4 2l4 4-4 4"/></svg></div>
  <div class="client" style="left:137px">Gearline</div>
  <div class="client" style="left:322px">Jobaxis</div>
  <div class="client" style="left:508px"><i></i>Northmark</div>
  <div class="client" style="left:694px">Techloom</div>
  <div class="client" style="left:881px">Aquaven</div>
</section>

<section class="cta">
  <div class="cta-halo"></div>
  <div class="cta-photo" role="img" aria-label="Two engineers holding a laptop and tablet"></div>
  <h2>Ready to Get Started?</h2>
  <p>Send Us Your Project Details And We'll Guide You<br>Through The Next Steps.</p>
  <a class="btn btn-blue">Contact Us</a>
</section>

<footer class="footer">
  <div class="footer-dark"></div>
  <div class="footer-photo" role="img" aria-label="Aerial view of a coastal town"></div>
  <div class="footer-nav">
    <a style="left:377px">Home</a>
    <a style="left:450px">Why Choose Us</a>
    <a style="left:590px">About Us</a>
    <a style="left:687px">Our Services</a>
    <a style="left:804px">Our Portfolio</a>
    <a style="left:925px">Contact Us</a>
  </div>
  <div class="f-item" style="left:381px"><div class="f-ico"><svg width="16" height="16" viewBox="0 0 24 24" fill="none" stroke="#3058e8" stroke-width="2"><path d="M12 22s7-7 7-12a7 7 0 0 0-14 0c0 5 7 12 7 12z"/><circle cx="12" cy="10" r="2.5"/></svg></div><div>Address<br>Eastmoor, UK</div></div>
  <div class="f-item" style="left:581px"><div class="f-ico"><svg width="16" height="16" viewBox="0 0 24 24" fill="none" stroke="#3058e8" stroke-width="2"><path d="M5 3h4l2 5-3 2a12 12 0 0 0 6 6l2-3 5 2v4a2 2 0 0 1-2 2A18 18 0 0 1 3 5a2 2 0 0 1 2-2z"/></svg></div><div>Call Us<br>+44 (0)7700 900 321</div></div>
  <div class="f-item" style="left:796px"><div class="f-ico"><svg width="16" height="16" viewBox="0 0 24 24" fill="none" stroke="#3058e8" stroke-width="2"><rect x="3" y="5" width="18" height="14"/><path d="M3 6l9 7 9-7"/></svg></div><div>Email Us<br>info@valtrobuild.design</div></div>
  <div class="copy">© 2026 Valtro Mechanical Design.</div>
  <div class="socials"><span></span><span></span><span></span><span></span></div>
</footer>

</div>
</body>
</html>
```